Female Pest Controller needs awesome business cards

I need a logo design for a Pest Control service - something that appeals to 'nature' & safe, with the use of the colour green. I am also female
New Business Name is 'Bug Begone Bay'
appeals to women

Target Market(s)

Domestic Households & Local Businesses

Industry/Entity Type

Pest Control

Contact Information for Business Card

Corinne Waldrake
0428316952
ABN 47 618 259 304
PMT7314958207
Spiders Cockroaches, Ants, Silverfish, Fleas, Rodents

Font styles to use
Decorative

Colors
abd036
aaaaaa
5c5c5c

Requirements
Should not have
• Pics of dead insects, prefer nature inspired designs, frogs, trees etc
• Have attached old log & business name ( now my ex's business) Lilyvale Pest Solutions -

```html
<!DOCTYPE html>
<html lang="en">
<head>
<meta charset="utf-8">
<title>Bug Begone Bay – Business Card</title>
<link rel="stylesheet" href="https://fonts.googleapis.com/css2?family=Arvo:wght@700&family=Lato:wght@400&display=swap">
<style>
  :root {
    --lime: #abd036;
    --slate: #5c5c5c;
    --mist: #aaaaaa;
    --white: #ffffff;
    --disc: #f4f4f2;
    --backdrop: #e8e8e5;
  }
  html, body {
    margin: 0;
    width: 1200px;
    height: 900px;
    overflow: hidden;
    background: var(--backdrop);
  }
  .business-card {
    position: absolute;
    left: 150px;
    top: 171px;
    width: 900px;
    height: 558px;
    background: var(--lime);
    overflow: hidden;
    box-shadow: 0 6px 22px rgba(0,0,0,0.18);
  }
  .side-band {
    position: absolute;
    left: 593px;
    top: 0;
    width: 307px;
    height: 100%;
    background: var(--slate);
  }
  .brand-disc {
    position: absolute;
    left: 367px;
    top: 34px;
    width: 482px;
    height: 482px;
    border-radius: 50%;
    background: var(--disc);
    display: flex;
    align-items: center;
    justify-content: center;
  }
  .brand-name {
    font-family: "Arvo", Georgia, serif;
    font-weight: 700;
    font-size: 44px;
    color: var(--slate);
    margin: 0;
    text-align: center;
    line-height: 1.15;
  }
  .contact {
    position: absolute;
    left: 54px;
    top: 58px;
    color: var(--white);
  }
  .contact-name {
    font-family: "Arvo", Georgia, serif;
    font-weight: 700;
    font-size: 26px;
    margin: 0 0 36px;
    letter-spacing: 0.3px;
  }
  .contact-details {
    font-family: "Lato", Arial, sans-serif;
    font-size: 24px;
    line-height: 34px;
    margin: 0;
  }
  .divider {
    position: absolute;
    left: 54px;
    top: 275px;
    width: 330px;
    height: 1px;
    background: rgba(255,255,255,0.55);
  }
  .services {
    position: absolute;
    left: 54px;
    top: 315px;
    margin: 0;
    padding: 0;
    list-style: none;
    font-family: "Lato", Arial, sans-serif;
    font-size: 24px;
    line-height: 32.6px;
    color: var(--white);
  }
  .services li::before {
    content: "";
    display: inline-block;
    width: 12px;
    height: 12px;
    border-radius: 50%;
    background: var(--white);
    margin-right: 7px;
    vertical-align: 2px;
  }
</style>
</head>
<body>
  <section class="business-card">
    <div class="side-band"></div>

    <div class="contact">
      <h1 class="contact-name">Corinne Waldrake</h1>
      <p class="contact-details">
        Phone:&nbsp; 0428316952<br>
        ABN: 47 618 259 304<br>
        PMT Lic: #73149582
      </p>
    </div>

    <div class="divider"></div>

    <ul class="services">
      <li>Spiders</li>
      <li>Cockroaches</li>
      <li>Ants</li>
      <li>Silverfish</li>
      <li>Fleas</li>
      <li>Rodents</li>
    </ul>

    <div class="brand-disc">
      <p class="brand-name">Bug Begone<br>Bay</p>
    </div>
  </section>
</body>
</html>
```